Flyer-Design für Lumira Afghan Take Away
Zielgruppe
Gastrobetrieb mit Afghanischer Küche. Hauptangebot: Reisgerichte, Teigtaschen und Korma (Currygerichte). ZG: Studenten/Schüller, Ladenbesitzer und Passanten, da es sehr Zentral liegt
Aufgabenstellung
Öffnungszeiten:
MO: 11:30-14h
DI&MI: 11:30-14h/18h-20h
DO&FR: 11:30-14h/18h-21h
SA: 11:30-15h
SO: Geschlossen
INFO: www.lumira-imbiss.ch

```html
<!DOCTYPE html>
<html lang="de">
<head>
<meta charset="utf-8">
<title>Lumira Afghan Take Away – Flyer</title>
<link rel="stylesheet" href="https://fonts.googleapis.com/css2?family=Roboto:wght@400;700;900&family=Questrial&family=Playfair+Display:ital,wght@1,700&display=swap">
<style>
  :root {
    --stage: #e8e8e8;
    --paper: #f2f2f2;
    --paper-dark: #dcdcdc;
    --ink: #1b1b1b;
    --ink-soft: #555;
    --red: #d21f26;
    --wine: #8a2826;
    --wine-dark: #6f1f1d;
    --green: #2d6b34;
    --black: #151515;
    --cream: #fbf7f2;
    --wood: #d9b48a;
  }
  * { box-sizing: border-box; margin: 0; padding: 0; }
  html, body { width: 1200px; height: 1200px; overflow: hidden; }
  body { background: var(--stage); font-family: "Roboto", Arial, sans-serif; position: relative; }

  .tricolor { display: flex; height: 12px; }
  .tricolor span { flex: 1; }
  .tricolor .c-black { background: var(--black); }
  .tricolor .c-red { background: var(--wine); }
  .tricolor .c-green { background: var(--green); }

  /* ---------- Menu card (tall) ---------- */
  .menu-card {
    position: absolute; left: 40px; top: 120px; width: 380px; height: 960px;
    background: linear-gradient(160deg, var(--paper) 0%, #e6e6e6 45%, var(--paper) 70%, var(--paper-dark) 100%);
    display: flex; flex-direction: column;
    box-shadow: 0 4px 14px rgba(0,0,0,.18);
  }
  .menu-card .corner { position: absolute; width: 26px; height: 26px; }
  .menu-card .corner.tl { left: 0; top: 12px; background: linear-gradient(135deg, var(--black) 50%, transparent 50%); }
  .menu-card .corner.tr { right: 0; top: 12px; background: linear-gradient(225deg, var(--green) 50%, transparent 50%); }
  .menu-body { flex: 1; padding: 52px 26px 0 30px; }
  .menu-heading { display: flex; justify-content: space-between; align-items: flex-end;
    color: var(--red); font-weight: 900; font-size: 15px; letter-spacing: .2px; margin-bottom: 6px; }
  .menu-heading small { color: var(--ink-soft); font-size: 8px; font-weight: 400; }
  .menu-heading + .menu-heading { margin-top: 24px; }
  .dish { display: grid; grid-template-columns: 38px 1fr 58px; border-bottom: 1px solid var(--red);
    padding: 4px 0 3px; }
  .dish .day { color: var(--red); font-weight: 900; font-size: 15px; line-height: 18px; }
  .dish .name { font-weight: 700; font-size: 15px; line-height: 18px; color: var(--ink); }
  .dish .desc { font-size: 8.5px; line-height: 10.5px; color: var(--ink-soft); margin-top: 1px; }
  .dish .price { align-self: end; text-align: right; font-weight: 700; font-size: 15px; color: var(--ink); }
  .menu-footer { height: 130px; background: var(--wine); display: flex; flex-direction: column;
    justify-content: center; padding-left: 30px; color: #fff; font-family: "Questrial", sans-serif; }
  .menu-footer .brand { font-size: 30px; letter-spacing: 2px; text-transform: uppercase; }
  .menu-footer .tag { font-size: 15px; margin-top: 4px; }

  /* ---------- Landscape flyer ---------- */
  .flyer {
    position: absolute; left: 460px; top: 441px; width: 700px; height: 318px;
    display: flex; box-shadow: 0 4px 14px rgba(0,0,0,.18);
  }
  .offers { width: 480px; background: var(--cream); display: flex; flex-direction: column; }
  .offers .tricolor { height: 7px; }
  .offer-grid { flex: 1; display: grid; grid-template-columns: 1fr 1fr; grid-template-rows: 1fr 1fr;
    gap: 10px; padding: 12px 14px; }
  .offer { position: relative; border-radius: 10px; overflow: hidden; padding: 10px 12px;
    background: linear-gradient(180deg, #f4efe9 0%, #ece4da 48%, var(--wood) 100%); }
  .offer h3 { color: var(--red); font-weight: 900; font-size: 13px; line-height: 15px; }
  .offer h3 .qty { font-weight: 400; }
  .offer p { color: var(--red); font-size: 8px; line-height: 10px; margin-top: 2px; max-width: 180px; }
  .offer .dish-photo { position: absolute; left: 40px; bottom: 10px; width: 112px; height: 56px;
    border-radius: 50%; background: radial-gradient(ellipse at center, #d9a46a 0%, #e9d3b8 45%, #ffffff 70%); }
  .offer .badge { position: absolute; right: 12px; bottom: 12px; width: 46px; height: 46px; border-radius: 50%;
    background: var(--red); color: #fff; display: flex; align-items: center; justify-content: center;
    font-family: "Playfair Display", serif; font-style: italic; font-weight: 700; font-size: 17px; }
  .info { flex: 1; background: var(--wine); color: #fff; font-family: "Questrial", sans-serif;
    padding: 28px 18px 20px 24px; display: flex; flex-direction: column; }
  .info .brand { font-size: 24px; letter-spacing: 2px; text-transform: uppercase; text-align: center; }
  .info .tag { font-size: 12px; text-align: center; margin-top: 2px; }
  .info h4 { font-weight: 400; font-size: 13px; text-decoration: underline; margin-top: 30px; margin-bottom: 8px; }
  .hours { list-style: none; font-size: 11px; line-height: 15px; }
  .hours b { font-weight: 400; letter-spacing: .3px; }
  .info .web { font-size: 11.5px; margin-top: 18px; }
  .address { display: flex; gap: 6px; margin-top: auto; font-size: 12.5px; line-height: 14px; }
  .address svg { flex: none; margin-top: 1px; }
</style>
</head>
<body>

<section class="menu-card">
  <div class="tricolor"><span class="c-black"></span><span class="c-red"></span><span class="c-green"></span></div>
  <span class="corner tl"></span><span class="corner tr"></span>
  <div class="menu-body">
    <h2 class="menu-heading">HAUSGEMACHTE MITTAGSMENÜ: <small>CHF</small></h2>
    <div class="dish"><span class="day">MO:</span><div><div class="name">Lawang</div><div class="desc">Pouletbrustgeschn. in Kurkuma-Joghurt-Sauce und frischen Kräuter, dazu Brechbohnen Qorma und Basmatireis</div></div><span class="price">14.50</span></div>
    <div class="dish"><span class="day">DI:</span><div><div class="name">Qorma Tschalau</div><div class="desc">Basmatireis mit würzigem Rindfleisch, dazu Sabzi (gebratener Spinat)</div></div><span class="price">14.50</span></div>
    <div class="dish"><span class="day">MI:</span><div><div class="name">Kofta Tschalau</div><div class="desc">Basmatireis mit Kofta (Afgh. Meatballs), Dal (Linsen)</div></div><span class="price">14.50</span></div>
    <div class="dish"><span class="day">DO:</span><div><div class="name">Kabuli-Palau mit Pouletfleisch</div><div class="desc">Brauner Basmatireis mit Karottenstreifen, Rosinen, gekochtem Pouletfleisch und Qorme-e Gulpi (Blumenkohl an Tomatensauce)</div></div><span class="price">14.50</span></div>
    <div class="dish"><span class="day"></span><div><div class="name">Kabuli-Palau mit Lamm-Qorma</div><div class="desc">Brauner Basmati-Reis mit Karottenstr., Rosinen, Lamm-Qorma und Qorme-e Gulpi (Blumenkohl an Tomatens.)</div></div><span class="price">16.50</span></div>
    <div class="dish"><span class="day">FR:</span><div><div class="name">Mahi Tschalau</div><div class="desc">Basmatireis mit Fisch-Quorma und Qorme-e Sabzi (gebratener Spinat mit Bohnen)</div></div><span class="price">14.50</span></div>
    <div class="dish"><span class="day"></span><div><div class="name">Lawang</div><div class="desc">Pouletgeschn. in Kurkuma-Joghurt-Sauce und fr. Kräuter, Qorme-e Sabzi (gebr. Spinat mit Bohnen), Basmatireis</div></div><span class="price">14.50</span></div>
    <div class="dish"><span class="day">SA:</span><div><div class="name">Kabuli-Palau mit Pouletfleisch</div><div class="desc">Brauner Basmatireis mit Karottenstreifen, Rosinen, gekochtem Pouletfleisch und Qorme-e Gulpi (Blumenkohl an Tomatensauce)</div></div><span class="price">14.50</span></div>
    <div class="dish"><span class="day"></span><div><div class="name">Kabuli-Palau mit Lamm-Qorma</div><div class="desc">Brauner Basmati-Reis mit Karottenstr., Rosinen, Lamm-Qorma und Qorme-e Gulpi (Blumenkohl an Tomatensauce)</div></div><span class="price">16.50</span></div>

    <h2 class="menu-heading">TÄGLICHES ANGEBOT:</h2>
    <div class="dish"><span class="day"></span><div><div class="name">Aushak Suppe</div><div class="desc">Linsensuppe mit Joghurt und Minze</div></div><span class="price">8.50</span></div>
    <div class="dish"><span class="day"></span><div><div class="name">Chapli-Kabob im Taschenbrot</div><div class="desc">Rindshacksteak mit Salat und Sauce</div></div><span class="price">9.-</span></div>
    <div class="dish"><span class="day"></span><div><div class="name">2 Sambosa</div><div class="desc">Chili-Koriander und Joghurt-Minze</div></div><span class="price">6.-</span></div>
    <div class="dish"><span class="day"></span><div><div class="name">Unser Salatteller</div><div class="desc">Mix aus Saisonsalat mit Kräutern</div></div><span class="price">7.50</span></div>
  </div>
  <footer class="menu-footer">
    <div class="brand">Lumira</div>
    <div class="tag">Take Away</div>
  </footer>
  <div class="tricolor"><span class="c-black"></span><span class="c-red"></span><span class="c-green"></span></div>
</section>

<section class="flyer">
  <div class="offers">
    <div class="tricolor"><span class="c-black"></span><span class="c-red"></span><span class="c-green"></span></div>
    <div class="offer-grid">
      <article class="offer">
        <h3>Chapli-Kabob im Taschenbrot</h3>
        <p>Gebratene Rindshacksteaks mit Gemüse, Salat, Chili-Koriander und Joghurt-Minze-Sauce</p>
        <div class="dish-photo" role="img" aria-label="Foto: Chapli-Kabob im Taschenbrot"></div>
        <span class="badge">9.-</span>
      </article>
      <article class="offer">
        <h3>Mantu</h3>
        <p>Gedämpfte Rindhackfleischtaschen aus frischem Teig, dazu Tomatensauce mit gelben Erbsen und Joghurt-Minze-Sauce</p>
        <div class="dish-photo" role="img" aria-label="Foto: Teller mit Mantu"></div>
        <span class="badge">14.-</span>
      </article>
      <article class="offer">
        <h3>Sambosa <span class="qty">2 Stk.</span></h3>
        <p>Frittierte Kartoffel oder Gemüsetaschen, dazu Chili-Koriandersauce und Joghurt-Minze-Sauce</p>
        <div class="dish-photo" role="img" aria-label="Foto: zwei Sambosa mit Saucen"></div>
        <span class="badge">6.-</span>
      </article>
      <article class="offer">
        <h3>Ashak</h3>
        <p>Gedämpfte Lauchtaschen aus frischem Teig, dazu Tomatensauce mit gelben Erbsen und Joghurt-Minze-Sauce</p>
        <div class="dish-photo" role="img" aria-label="Foto: Teller mit Ashak"></div>
        <span class="badge">14.-</span>
      </article>
    </div>
    <div class="tricolor" style="height:7px"><span class="c-red"></span><span class="c-green"></span><span class="c-black"></span></div>
  </div>
  <aside class="info">
    <div class="brand">Lumira</div>
    <div class="tag">Take Away</div>
    <h4>Öffnungszeiten:</h4>
    <ul class="hours">
      <li><b>MO:</b> 11:30-14h</li>
      <li><b>DI&amp;MI:</b> 11:30-14h/18h-20h</li>
      <li><b>DO&amp;FR:</b> 11:30-14h/18h-21h</li>
      <li><b>SA:</b> 11:30-15h</li>
      <li><b>SO:</b> Geschlossen</li>
    </ul>
    <div class="web">www.lumira-imbiss.ch</div>
    <div class="address">
      <svg width="12" height="16" viewBox="0 0 12 16" aria-hidden="true"><path d="M6 0C2.7 0 0 2.6 0 5.9 0 10.3 6 16 6 16s6-5.7 6-10.1C12 2.6 9.3 0 6 0zm0 8.3a2.4 2.4 0 1 1 0-4.8 2.4 2.4 0 0 1 0 4.8z" fill="#fff"/></svg>
      <div>Talackerweg 21<br>8001 Zürich</div>
    </div>
  </aside>
</section>

</body>
</html>
```